Brindlo Wordpress Website

We require a WordPress website that emulates the sleek design and functionality of https://www.quorvexa.com and https://tolmindo.ai/. The site should showcase our AI-powered customer support solutions with a modern, professional aesthetic.
Homepage
The homepage should feature a bold headline highlighting our AI capabilities, followed by concise sections outlining our key offerings:
AI-powered customer support
Data integration and deployment
Knowledge system integration
AI help desks and chat agents
Customer feedback insights
Include eye-catching visuals or animations to illustrate these concepts.
Navigation
The main navigation menu should include:
Product
Platform
Company
News
Learn More
Key Pages
Product Page: Detail our AI solutions, their benefits, and use cases.
Platform Page: Explain our technology, integration capabilities, and deployment process.
Company Page: Share our mission, team, and values.
News Page: Feature latest updates, press releases, and blog posts.
Call-to-Action
Implement a prominent "Learn More" button that directs users to an enrollment page. Our team will manage inquiries from this point.
Footer
Include a "Contact Us" section in the footer for easy access to our contact information.
Design Elements
Use a clean, minimalist design with ample white space
Incorporate a color scheme that reflects trust and innovation
Utilize smooth scrolling and subtle animations for enhanced user experience
Ensure mobile responsiveness for all devices
Technical Requirements
Build on WordPress for easy content management
Optimize for fast loading speeds and SEO
The website should convey our expertise in AI-driven customer support solutions while providing an intuitive user experience that guides visitors toward learning more about our services

```html
<!DOCTYPE html>
<html lang="en">
<head>
<meta charset="utf-8">
<title>Brindlo – Meet Brindlo</title>
<link href="https://fonts.googleapis.com/css2?family=Outfit:wght@300;400;500&display=swap" rel="stylesheet">
<style>
:root{
  --ink:#1c2b2f;
  --ink-soft:#4e5d61;
  --night:#15313a;
  --teal:#3b8087;
  --teal-deep:#2a5f66;
  --mist:#eef2f3;
  --feature:#e9eff0;
  --white:#ffffff;
  --line:#c9d2d4;
}
*{box-sizing:border-box;margin:0;padding:0}
html,body{width:1200px;height:4091px;overflow:hidden}
body{position:relative;background:var(--white);font-family:"Outfit",sans-serif;color:var(--ink)}
.abs{position:absolute}
.btn{position:absolute;display:flex;align-items:center;justify-content:center;background:var(--teal);color:var(--white);border-radius:30px;font-size:19px;font-weight:500;letter-spacing:.3px;text-transform:uppercase}

/* hero */
.hero-band{left:0;top:0;width:1200px;height:556px;background:var(--night)}
.brand{display:flex;align-items:center;gap:12px;color:var(--white);font-weight:400}
.brand-dot{border-radius:50%;background:var(--teal)}
.nav{left:403px;top:40px;display:flex;gap:27px;font-size:19px;color:var(--white)}
.nav .active{color:#6fb3b8}
.hero-title{left:0;top:122px;width:1200px;text-align:center;color:var(--white);font-size:70px;font-weight:400}
.slide{top:275px;height:488px;border-radius:32px;background:linear-gradient(160deg,#cdb9a2,#8e7a66 55%,#e6e2dd)}
.slide-cap{position:absolute;top:22px;color:var(--white);font-size:21px;font-weight:500;white-space:nowrap}
.dots{left:575px;top:807px;display:flex;gap:6px}
.dots span{width:11px;height:11px;border-radius:50%;border:1.5px solid #8a9599}
.dots span.on{background:#5c6a6e;border-color:#5c6a6e}

/* interactions */
.sec-title{font-size:44px;font-weight:400;line-height:54px;color:var(--ink)}
.feature{left:111px;width:381px}
.feature-box{background:var(--feature);border-radius:10px}
.feature h3{position:absolute;left:114px;font-size:22px;font-weight:500}
.feature p{position:absolute;left:114px;font-size:17px;line-height:25px;color:var(--ink-soft);font-weight:300}
.feature svg{position:absolute;left:20px}
.demo{left:619px;top:1009px;width:511px;height:526px;border-radius:34px;background:linear-gradient(180deg,#3a7b81,#1f4d55)}
.demo-input{position:absolute;left:32px;top:40px;width:454px;height:37px;background:var(--white);font-size:11px;font-weight:500;padding:11px 14px}
.demo-input i{position:absolute;right:12px;top:7px;width:24px;height:24px;border-radius:50%;background:var(--teal)}
.demo-panel{position:absolute;left:43px;top:99px;width:431px;height:384px;background:var(--white);padding:50px 30px;font-size:38px;line-height:45px;font-weight:300}
.play{position:absolute;width:52px;height:52px;border-radius:50%;background:var(--white);box-shadow:0 2px 8px rgba(0,0,0,.18)}
.play::after{content:"";position:absolute;left:20px;top:16px;border-left:16px solid var(--ink);border-top:10px solid transparent;border-bottom:10px solid transparent}

/* showcase */
.showcase{left:0;top:1650px;width:1200px;height:2048px;background:linear-gradient(180deg,#e5ebec 0%,#f7f9f9 40%,#eef2f2 100%)}
.card{width:511px;height:485px;border-radius:30px;background:radial-gradient(circle at 50% 40%,#ffffff 40%,#e3e8e9 100%)}
.shot{position:absolute;border-radius:4px;background:linear-gradient(180deg,#fbfcfc,#eef1f2);box-shadow:0 2px 10px rgba(0,0,0,.12)}
.body-text{font-size:19px;line-height:28px;color:var(--ink-soft);font-weight:300}
.trust{left:692px;width:440px;display:flex;align-items:center}
.trust svg{position:absolute;left:0}
.trust p{position:absolute;left:86px;font-size:18px;line-height:28px;color:var(--ink-soft);font-weight:300;width:340px}

/* footer */
.foot-col{font-size:18px;line-height:32px;color:var(--ink-soft);font-weight:300}
.contact{font-size:17px;color:var(--ink-soft);font-weight:300;display:flex;align-items:center;gap:8px}
.rule{left:111px;top:4000px;width:978px;height:1px;background:var(--line)}
.copy{left:0;top:4031px;width:1200px;text-align:center;font-size:17px;color:var(--ink-soft);font-weight:300}
</style>
</head>
<body>

<!-- hero -->
<div class="abs hero-band"></div>
<div class="abs brand" style="left:111px;top:17px;font-size:40px">
  <span class="brand-dot" style="width:64px;height:64px"></span>Brindlo
</div>
<nav class="abs nav">
  <span class="active">Home</span><span>Product</span><span>Platform</span><span>Company</span><span>News</span>
</nav>
<a class="btn" style="left:938px;top:27px;width:152px;height:56px">Learn more</a>
<h1 class="abs hero-title">Meet Brindlo</h1>

<div class="abs slide" style="left:-130px;width:301px" role="img" aria-label="Photo of a laptop on a desk in a bright room">
  <span class="slide-cap" style="right:36px">'s AI Assistant</span>
</div>
<div class="abs slide" style="left:227px;width:746px" role="img" aria-label="Photo of a woman working on a laptop at a home desk">
  <span class="slide-cap" style="left:48px">Elevate your users' experience, a new type of conversation awaits</span>
</div>
<div class="abs slide" style="left:1024px;width:300px;background:linear-gradient(160deg,#9a5b3f,#3c2a22 60%,#d8d2cb)" role="img" aria-label="Photo of an office chair beside a brick wall">
  <span class="slide-cap" style="left:51px">Always ready</span>
</div>
<div class="abs dots"><span></span><span class="on"></span><span></span></div>

<!-- interactions -->
<h2 class="abs sec-title" style="left:108px;top:925px">Revolutionize your<br>customer interactions</h2>

<div class="abs feature feature-box" style="top:1095px;height:129px">
  <svg width="64" height="56" viewBox="0 0 64 56" style="top:20px" fill="none" stroke="#2a5f66" stroke-width="2.4"><path d="M6 8h30v20H18l-8 7v-7H6z"/><path d="M28 30h30v18h-4v6l-7-6H28z"/><circle cx="20" cy="18" r="4"/></svg>
  <h3 style="top:18px">Get answers</h3>
  <p style="top:52px">Users will find the information<br>they need in seconds</p>
</div>
<div class="abs feature" style="top:1253px;height:110px">
  <svg width="64" height="70" viewBox="0 0 64 70" style="top:12px" fill="none" stroke="#2a5f66" stroke-width="2.4"><rect x="14" y="6" width="20" height="20"/><rect x="34" y="22" width="20" height="20"/><rect x="10" y="32" width="22" height="16"/><path d="M8 68V56h10v12M26 68V56h10v12"/></svg>
  <h3 style="top:15px">Solve problems</h3>
  <p style="top:49px">Concerns will be addressed<br>quickly with expert assistance</p>
</div>
<div class="abs feature" style="top:1388px;height:160px">
  <svg width="64" height="70" viewBox="0 0 64 70" style="top:8px" fill="none" stroke="#2a5f66" stroke-width="2.4"><path d="M4 24a22 22 0 0 1 36-14"/><path d="M34 4l6 6-7 4"/><path d="M18 30l16 22c4 6 14 8 18 0 3-6-2-12-8-14l-8-2-8-10c-3-4-9 0-10 4z"/></svg>
  <h3 style="top:15px">Take action</h3>
  <p style="top:49px">Users will activate services and<br>features immediately<br>All through natural,<br>conversational experiences</p>
</div>

<div class="abs demo">
  <div class="demo-input">How do i promote my July wine tour?<i></i></div>
  <div class="demo-panel">Lorem ipsum dolor sit amet, consecte litur adipiscing elit, sed do eiusmod tempor inci didunt ut labore et dolore magna.</div>
  <span class="play" style="left:434px;top:443px"></span>
</div>

<!-- showcase -->
<div class="abs showcase"></div>

<div class="abs card" style="left:86px;top:1750px">
  <div class="shot" style="left:102px;top:86px;width:323px;height:280px" role="img" aria-label="Screenshot of a knowledge issue dashboard"></div>
  <div class="shot" style="left:90px;top:228px;width:214px;height:186px" role="img" aria-label="Screenshot of a help center article review"></div>
  <span class="play" style="left:433px;top:398px"></span>
</div>
<h2 class="abs sec-title" style="left:692px;top:1811px">Brindlo enables<br>you to</h2>
<p class="abs body-text" style="left:692px;top:1952px;width:430px">Engage and delight customers with an AI agent aligned to your brand Provide real-time support for a wide variety of uses from simple to complex</p>
<a class="btn" style="left:693px;top:2079px;width:161px;height:57px">Learn more</a>

<h2 class="abs sec-title" style="left:113px;top:2360px">Make AI your own<br>with Brindlo's<br>conversational<br>platform</h2>
<p class="abs body-text" style="left:113px;top:2609px;width:430px">Ground your Brindlo AI agent in your company's identity and knowledge Solve problems quickly and effectively</p>
<a class="btn" style="left:113px;top:2738px;width:169px;height:56px">Learn more</a>
<div class="abs card" style="left:603px;top:2341px">
  <div class="shot" style="left:102px;top:75px;width:323px;height:280px" role="img" aria-label="Screenshot of a knowledge issue dashboard"></div>
  <div class="shot" style="left:163px;top:75px;width:200px;height:178px" role="img" aria-label="Screenshot of a help center article review"></div>
  <span class="play" style="left:433px;top:398px"></span>
</div>

<div class="abs card" style="left:86px;top:2933px">
  <div class="shot" style="left:102px;top:86px;width:323px;height:280px" role="img" aria-label="Screenshot of a knowledge issue dashboard"></div>
  <div class="shot" style="left:90px;top:228px;width:214px;height:186px" role="img" aria-label="Screenshot of a help center article review"></div>
  <span class="play" style="left:433px;top:398px"></span>
</div>
<h2 class="abs sec-title" style="left:692px;top:2993px">Brindlo prioritizes<br>trust and security</h2>

<div class="abs trust" style="top:3144px;height:60px">
  <svg width="56" height="60" viewBox="0 0 56 60" fill="none" stroke="#2a5f66" stroke-width="2.2"><path d="M10 4h26l10 10v42H10z"/><path d="M18 48V38M25 48V32M32 48V40M39 48V34"/><circle cx="16" cy="14" r="8"/></svg>
  <p style="top:16px">Built-in supervision and auditing</p>
</div>
<div class="abs trust" style="top:3228px;height:60px">
  <svg width="60" height="60" viewBox="0 0 60 60" fill="none" stroke="#2a5f66" stroke-width="2.2"><rect x="4" y="26" width="26" height="22" rx="3"/><path d="M10 26v-8a7 7 0 0 1 14 0v8"/><path d="M30 30h14l6-6M30 38h20M30 44h14l6 6"/><circle cx="54" cy="22" r="3"/><circle cx="54" cy="38" r="3"/><circle cx="54" cy="52" r="3"/></svg>
  <p style="top:16px">Secure integrations</p>
</div>
<div class="abs trust" style="top:3312px;height:64px">
  <svg width="60" height="64" viewBox="0 0 60 64" fill="none" stroke="#2a5f66" stroke-width="2.2"><rect x="4" y="4" width="34" height="48"/><path d="M10 14h22M10 22h22M10 30h16"/><circle cx="40" cy="46" r="12"/><path d="M34 46l4 4 8-8"/></svg>
  <p style="top:18px">Strong data governance and privacy</p>
</div>
<div class="abs trust" style="top:3412px;height:84px">
  <svg width="66" height="70" viewBox="0 0 66 70" fill="none" stroke="#2a5f66" stroke-width="2.2"><path d="M33 4l3 6 6 1-4 4 1 6-6-3-6 3 1-6-4-4 6-1z"/><path d="M10 14l2 4 4 1-3 3 1 4-4-2-4 2 1-4-3-3 4-1zM56 14l2 4 4 1-3 3 1 4-4-2-4 2 1-4-3-3 4-1z"/><circle cx="33" cy="38" r="8"/><path d="M18 68v-6c0-8 6-12 15-12s15 4 15 12v6z"/></svg>
  <p style="top:0">Discover how Brindlo can transform your customer experience with customized conversational AI.</p>
</div>
<a class="btn" style="left:694px;top:3544px;width:168px;height:57px">Learn more</a>

<!-- footer -->
<div class="abs brand" style="left:105px;top:3768px;font-size:56px;color:var(--ink)">
  <span class="brand-dot" style="width:86px;height:86px"></span>Brindlo
</div>
<div class="abs contact" style="left:110px;top:3886px">
  <svg width="12" height="16" viewBox="0 0 12 16"><path d="M6 0a6 6 0 0 0-6 6c0 4 6 10 6 10s6-6 6-10a6 6 0 0 0-6-6z" fill="#3b8087"/><circle cx="6" cy="6" r="2" fill="#fff"/></svg>
  123 Lorem 3rd Floor, Halvery, MA 11111
</div>
<div class="abs contact" style="left:110px;top:3925px">
  <svg width="14" height="14" viewBox="0 0 14 14"><path d="M3 0l3 3-2 2c1 2 3 4 5 5l2-2 3 3-2 3C6 14 0 8 0 3z" fill="#3b8087"/></svg>
  1 555 204 7381
</div>

<div class="abs foot-col" style="left:509px;top:3788px">Home<br>Product<br>Platform<br>Company<br>News</div>
<div class="abs foot-col" style="left:681px;top:3788px">Terms &amp; Conditions<br>Privacy Policy<br>Cookie Preferences</div>
<div class="abs foot-col" style="left:938px;top:3788px">
  <div style="display:flex;align-items:center;gap:10px"><span style="width:14px;height:14px;border-radius:50%;background:var(--teal)"></span>Linkora</div>
  <div style="display:flex;align-items:center;gap:10px"><span style="width:14px;height:14px;border-radius:50%;background:var(--teal)"></span>Chirpline</div>
</div>

<div class="abs rule"></div>
<p class="abs copy">© 2024 Brindlo. All rights reserved.</p>

</body>
</html>
```